Velder Auto Repair - Flyer Design

My business is a automobile shop where we fix cars. Such things that we do but not limited to is brakes, Engine/Transmission change, Electrical work, emission test, oil change and automobile diagnostic. I am looking for a flyer that will catch peoples attention, I will be giving flyers to people, putting them in car windows and mailboxes. I am looking for a flier that will help to attract more customers to my business. I also want the flyer to say "Bring in your estimate from our competitors with this flyer and we will beat it by 10%" (does not have to be in those exact words). I also want the flyer to have my business address phone and operating hours. I have attached a business card and my business ad which I have placed in the newspaper before. I hope it helps with your design.
Industry/Entity Type
Car Repair
Look and feel

```html
<!DOCTYPE html>
<html lang="en">
<head>
<meta charset="utf-8">
<title>Velder Auto Repair – Flyer</title>
<link rel="stylesheet" href="https://fonts.googleapis.com/css2?family=Cinzel:wght@700&family=Oswald:wght@600&family=Roboto:wght@300;400;500&family=Roboto+Condensed:wght@700&display=swap">
<style>
  :root {
    --page-bg: #ffffff;
    --sheet-edge: #efeeea;
    --sheet-fill: #e2e1dc;
    --ink-dark: #1d2527;
    --ink-grey: #4f4f4f;
    --tick-grey: #555555;
    --accent-pink: #d8175a;
    --dash: #8a8a8a;
    --panel-light: rgba(230, 230, 228, 0.82);
  }
  * { margin: 0; padding: 0; box-sizing: border-box; }
  html, body { width: 1200px; height: 1000px; overflow: hidden; background: var(--page-bg); }
  .flyer { position: absolute; left: 250px; top: 0; width: 702px; height: 1000px; background: var(--sheet-edge); }
  .coupon-frame {
    position: absolute; left: 22px; top: 22px; width: 658px; height: 953px;
    background: var(--sheet-fill); border: 2px dashed var(--dash);
  }
  .brand { position: absolute; left: 0; top: 40px; width: 702px; text-align: center; }
  .brand-name { font-family: "Cinzel", serif; font-weight: 700; font-size: 36px; color: var(--ink-dark); letter-spacing: 0.5px; line-height: 1; }
  .brand-tagline { font-family: "Cinzel", serif; font-weight: 700; font-size: 14px; color: var(--ink-dark); margin-top: 8px; letter-spacing: 0.3px; }
  .hero-photo {
    position: absolute; left: 0; top: 120px; width: 702px; height: 470px;
    background: linear-gradient(135deg, #2a2a2a 0%, #5a5a5a 35%, #1a1a1a 60%, #6e6e6e 85%, #202020 100%);
  }
  .offer-panel {
    position: absolute; left: 352px; top: 222px; width: 350px; height: 235px;
    background: var(--panel-light); text-align: right; padding: 24px 18px 0 0;
    font-family: "Roboto", sans-serif; color: var(--ink-dark);
  }
  .offer-lead { font-weight: 300; font-size: 30px; line-height: 1; }
  .offer-and { font-weight: 500; font-size: 21px; margin-top: 8px; }
  .offer-deal { font-family: "Oswald", sans-serif; font-weight: 600; font-size: 52px; color: var(--accent-pink); line-height: 1.05; margin-top: 2px; }
  .offer-terms { font-weight: 500; font-size: 22px; line-height: 1.25; margin-top: 8px; }
  .services { position: absolute; left: 0; top: 0; width: 702px; height: 1000px; list-style: none; }
  .service { position: absolute; display: flex; align-items: center; gap: 8px;
    font-family: "Cinzel", serif; font-weight: 700; font-size: 21px; color: var(--ink-dark); }
  .service svg { width: 34px; height: 30px; flex: none; }
  .contact-col { position: absolute; top: 822px; width: 230px; text-align: center; font-family: "Roboto", sans-serif; }
  .contact-icon { width: 68px; height: 68px; display: block; margin: 0 auto; }
  .contact-title { font-family: "Roboto Condensed", sans-serif; font-weight: 700; font-size: 19px; color: var(--accent-pink); margin-top: 14px; }
  .contact-line { font-size: 14px; color: var(--ink-grey); line-height: 19px; }
  .divider { position: absolute; top: 908px; width: 2px; height: 54px; background: var(--ink-dark); }
</style>
</head>
<body>
<main class="flyer">
  <div class="coupon-frame"></div>

  <header class="brand">
    <h1 class="brand-name">VELDER AUTO REPAIR</h1>
    <p class="brand-tagline">SPECIALIZING IN FOREIGN &amp; DOMESTIC CARS</p>
  </header>

  <div class="hero-photo" role="img" aria-label="Close-up photo of a socket wrench set with chrome sockets and a ratchet in a black case"></div>

  <section class="offer-panel">
    <p class="offer-lead">Show This Flyer</p>
    <p class="offer-and">and</p>
    <p class="offer-deal">GET 10% OFF</p>
    <p class="offer-terms">from any estimate<br>from our competitors</p>
  </section>

  <svg width="0" height="0" style="position:absolute">
    <defs>
      <symbol id="tick" viewBox="0 0 34 30"><path d="M2 16 L8 10 L14 17 L28 2 L33 8 L14 28 Z" fill="var(--tick-grey)"/></symbol>
      <radialGradient id="bubble" cx="40%" cy="30%" r="70%">
        <stop offset="0" stop-color="#ffffff"/><stop offset="0.6" stop-color="#dcdcdc"/><stop offset="1" stop-color="#a9a9a9"/>
      </radialGradient>
    </defs>
  </svg>

  <ul class="services">
    <li class="service" style="left:48px;top:630px"><svg><use href="#tick"/></svg>OIL CHANGE</li>
    <li class="service" style="left:306px;top:630px"><svg><use href="#tick"/></svg>ELECTRICAL WORK</li>
    <li class="service" style="left:48px;top:687px"><svg><use href="#tick"/></svg>EMISSION TEST</li>
    <li class="service" style="left:306px;top:687px"><svg><use href="#tick"/></svg>AUTOMOBILE DIAGNOSTIC</li>
    <li class="service" style="left:48px;top:744px"><svg><use href="#tick"/></svg>BRAKES, ENGINE &amp; TRANSMISSION CHANGE</li>
  </ul>

  <section class="contact-col" style="left:5px">
    <svg class="contact-icon" viewBox="0 0 68 68">
      <circle cx="34" cy="34" r="32" fill="url(#bubble)" stroke="#9a9a9a"/>
      <path d="M18 34 L34 20 L50 34 L46 34 L46 48 L38 48 L38 39 L30 39 L30 48 L22 48 L22 34 Z" fill="#111"/>
    </svg>
    <h2 class="contact-title">Bring Us Your Car</h2>
    <p class="contact-line">4270 S. Harbor Ave.</p>
    <p class="contact-line">Lakeview IL. 60999</p>
  </section>
  <div class="divider" style="left:233px"></div>

  <section class="contact-col" style="left:237px">
    <svg class="contact-icon" viewBox="0 0 68 68">
      <circle cx="34" cy="34" r="32" fill="url(#bubble)" stroke="#9a9a9a"/>
      <rect x="17" y="20" width="12" height="26" rx="2" fill="none" stroke="#111" stroke-width="2.5"/>
      <rect x="25" y="32" width="24" height="16" fill="#eee" stroke="#111" stroke-width="2.5"/>
      <path d="M25 32 L37 41 L49 32" fill="none" stroke="#111" stroke-width="2.5"/>
    </svg>
    <h2 class="contact-title">Contact Us</h2>
    <p class="contact-line">(555) 214 - 0387</p>
    <p class="contact-line">VelderAutoRepair@mail.com</p>
  </section>
  <div class="divider" style="left:467px"></div>

  <section class="contact-col" style="left:468px">
    <svg class="contact-icon" viewBox="0 0 68 68">
      <circle cx="34" cy="34" r="32" fill="url(#bubble)" stroke="#9a9a9a"/>
      <circle cx="34" cy="34" r="15" fill="none" stroke="#111" stroke-width="4"/>
      <path d="M34 25 L34 35 L41 35" fill="none" stroke="#111" stroke-width="3.5"/>
    </svg>
    <h2 class="contact-title">Operation Hours</h2>
    <p class="contact-line">Monday - Friday : 8am - 5pm</p>
    <p class="contact-line">Saturday : 8am - 1pm</p>
  </section>
</main>
</body>
</html>
```